Stonebay Towing Business Card

Towing
Accident towing
Mechanical breakdown
Insurance, salvage and recovery
4wd off road towing
Light & Heavy towing
8347 2516
24 hour business 7 days

Logo can be whole size on front

Industry/Entity Type

Towing/ transport

Contact Information for Business Card

The above

```html
<!DOCTYPE html>
<html lang="en">
<head>
<meta charset="utf-8">
<title>Stonebay Towing Business Card</title>
<link href="https://fonts.googleapis.com/css2?family=Poppins:wght@400;500;700&family=Michroma&display=swap" rel="stylesheet">
<style>
  :root {
    --brand-red: #cc1f26;
    --ink-black: #111111;
    --paper-white: #ffffff;
    --text-dark: #1c1c1c;
    --backdrop: #2b2b2d;
  }
  html, body {
    margin: 0;
    width: 1200px;
    height: 900px;
    overflow: hidden;
    background: var(--backdrop);
  }
  .card-stage {
    position: relative;
    width: 1200px;
    height: 900px;
  }
  .card {
    position: absolute;
    left: 270px;
    width: 660px;
    height: 377px;
    border-radius: 22px;
    overflow: hidden;
  }
  .card-front {
    top: 48px;
    background: var(--brand-red);
    display: flex;
    align-items: center;
    justify-content: center;
  }
  .front-name {
    font-family: "Poppins", sans-serif;
    font-weight: 700;
    font-size: 64px;
    color: var(--paper-white);
    letter-spacing: 1px;
  }
  .card-back {
    top: 475px;
    background: var(--paper-white);
  }
  .back-shapes {
    position: absolute;
    inset: 0;
  }
  .back-name {
    position: absolute;
    left: 34px;
    top: 52px;
    font-family: "Poppins", sans-serif;
    font-weight: 700;
    font-size: 38px;
    line-height: 1.2;
    color: var(--brand-red);
  }
  .back-name-faint {
    position: absolute;
    left: 20px;
    top: 236px;
    font-family: "Poppins", sans-serif;
    font-weight: 700;
    font-size: 34px;
    line-height: 1.2;
    color: var(--brand-red);
    opacity: 0.06;
  }
  .call-line {
    position: absolute;
    left: 22px;
    top: 169px;
    font-family: "Michroma", sans-serif;
    font-size: 17px;
    line-height: 1.5;
    color: var(--paper-white);
    letter-spacing: 1px;
  }
  .services-title {
    position: absolute;
    right: 62px;
    top: 184px;
    font-family: "Poppins", sans-serif;
    font-weight: 500;
    font-size: 19px;
    line-height: 26px;
    color: var(--brand-red);
  }
  .services-list {
    position: absolute;
    right: 40px;
    top: 216px;
    margin: 0;
    padding: 0;
    list-style: none;
    text-align: right;
    font-family: "Poppins", sans-serif;
    font-size: 14px;
    line-height: 17px;
    color: var(--text-dark);
  }
  .services-list li {
    white-space: nowrap;
  }
  .services-list li::after {
    content: "";
    display: inline-block;
    width: 6px;
    height: 6px;
    margin-left: 14px;
    border-radius: 50%;
    background: var(--brand-red);
    vertical-align: middle;
  }
  .hours-line {
    position: absolute;
    right: 60px;
    bottom: 16px;
    font-family: "Poppins", sans-serif;
    font-size: 16px;
    line-height: 1.5;
    color: var(--paper-white);
  }
</style>
</head>
<body>
<main class="card-stage">
  <section class="card card-front" aria-label="Card front">
    <span class="front-name">Stonebay Towing</span>
  </section>

  <section class="card card-back" aria-label="Card back">
    <svg class="back-shapes" width="660" height="377" viewBox="0 0 660 377" aria-hidden="true">
      <polygon class="call-band" points="0,155 310,155 285,210 0,210" fill="var(--brand-red)"/>
      <polygon class="services-band" points="310,150 660,150 660,180 296,180" fill="var(--ink-black)"/>
      <polygon class="services-tab" points="605,180 660,180 660,210 620,210" fill="var(--ink-black)"/>
      <rect class="base-stripe" x="0" y="343" width="280" height="8" fill="var(--brand-red)"/>
      <polygon class="hours-band" points="270,324 660,324 660,377 240,377" fill="var(--brand-red)"/>
    </svg>
    <span class="back-name">Stonebay Towing</span>
    <span class="back-name-faint" aria-hidden="true">Stonebay Towing</span>
    <span class="call-line">CALL US 8347 2516</span>
    <span class="services-title">Our Services</span>
    <ul class="services-list">
      <li>Towing</li>
      <li>Accident towing</li>
      <li>Mechanical breakdown</li>
      <li>Insurance, salvage and recovery</li>
      <li>4wd off road towing</li>
      <li>Light &amp; Heavy towing</li>
    </ul>
    <span class="hours-line">24 hour business 7 days</span>
  </section>
</main>
</body>
</html>
```